IT supplier clean wordpress website - payment guaranteed

Clean website design for a wordpress based website
Design only - PSD delivery with images

current website: www.quilmo.net
please use your imagination and try something out of the box...
We like https://trevanly.com.au as look and feel, but you don't have to copy it, you can be creative

We like the navigation header and the phone number, but do not need 'instant quote' so the 1300 phone number and the 'lock' icon for login can be on the same line

Site Map:
IT support
VoIP
Internet and Data
Cloud hosting
About
Contact

Our logo is attached, it can be used light or dark.
Our only color used is the warm grey Pantone 8003C hex #877A69

You will only need to design the homepage to win the competition, but the winning designer will be required to supply without extra charges:
1. Home page design
2. A second, standard page template design
3. An icon set in colors appropriate to the site that have icons to match the subjects in these pages:
https://trevanly.com.au/products/
https://trevanly.com.au/making-the-switch/
https://trevanly.com.au/why-trevanly/
We will create a single page version of the options on https://trevanly.com.au/solutions/
4.Any images used

Please avoid stock photos that are too common - e.g. smiling woman with headset, try to make the design stand out with simple images and well-designed layout.

Mid-size business clients

It Company

1 page

• Quil logo
• Use Quil color

```html
<!DOCTYPE html>
<html lang="en">
<head>
<meta charset="utf-8">
<title>Quil – IT outsourcing the way it should be</title>
<link href="https://fonts.googleapis.com/css2?family=Open+Sans:wght@300;400;600;700&family=Oswald:wght@400;600&display=swap" rel="stylesheet">
<style>
:root{
  --warm-grey:#877A69;
  --warm-dark:#6e6254;
  --charcoal:#2b2b2b;
  --footer:#2f2f2f;
  --text:#555;
  --light:#f3f2f0;
  --line:#d8d4cf;
  --white:#fff;
}
*{box-sizing:border-box;margin:0;padding:0}
html,body{width:1200px;height:2204px;overflow:hidden}
body{font-family:"Open Sans",Arial,sans-serif;color:var(--text);background:var(--white);position:relative}
.site-header{position:absolute;top:0;left:0;width:1200px;height:120px;background:var(--white)}
.brand{position:absolute;left:40px;top:26px;display:flex;align-items:center;gap:12px}
.brand-mark{width:22px;height:22px;background:var(--warm-grey)}
.brand-name{font-size:34px;font-weight:600;color:var(--warm-grey)}
.top-bar{position:absolute;right:40px;top:14px;display:flex;align-items:center;gap:14px;font-size:15px;color:#777}
.top-bar .phone{display:flex;align-items:center;gap:6px}
.login{background:var(--warm-grey);color:var(--white);padding:4px 12px;font-size:14px;display:flex;gap:6px;align-items:center}
.main-nav{position:absolute;right:40px;top:62px;display:flex;gap:40px;font-size:16px;color:#444}
.main-nav span:first-child{color:var(--warm-grey)}
.hero{position:absolute;top:120px;left:0;width:1200px;height:500px;
  background:
    radial-gradient(ellipse 260px 150px at 560px 250px,#fbfbfa 0%,rgba(251,251,250,0) 100%),
    radial-gradient(ellipse 120px 70px at 330px 190px,#f4f3f1 0%,rgba(244,243,241,0) 100%),
    radial-gradient(ellipse 110px 65px at 1010px 190px,#f1f0ee 0%,rgba(241,240,238,0) 100%),
    radial-gradient(ellipse 220px 260px at 80px 230px,#3c3a38 0%,rgba(60,58,56,0) 100%),
    radial-gradient(ellipse 240px 260px at 1140px 260px,#4a4744 0%,rgba(74,71,68,0) 100%),
    linear-gradient(180deg,#bdbab5 0%,#d9d7d3 40%,#c9c5bf 100%);
  border-bottom:4px solid var(--warm-grey)}
.intro{position:absolute;top:660px;left:80px;width:1040px;text-align:center}
.intro h1{font-weight:300;font-size:42px;color:#444;margin-bottom:28px}
.intro p{font-size:14px;line-height:22px;color:#666}
.services{position:absolute;top:860px;left:80px;width:1040px;display:flex;gap:22px}
.service{flex:1}
.service-image{height:200px;background:linear-gradient(135deg,#c8c2ba,#8d8479)}
.service:nth-child(2) .service-image{background:linear-gradient(135deg,#9aa3ab,#5d6670)}
.service:nth-child(3) .service-image{background:linear-gradient(135deg,#d2cdc6,#8a8279)}
.service-body{height:220px;background:var(--warm-grey);color:var(--white);text-align:center;padding:22px 26px}
.service:nth-child(2) .service-body{background:var(--warm-dark)}
.service-body h2{font-size:22px;font-weight:700;margin-bottom:12px}
.service-body p{font-size:14px;line-height:20px;color:#f1ece6}
.projects{position:absolute;top:1290px;left:0;width:1200px;height:330px;background:linear-gradient(180deg,#6a6a6a 0%,#3a3a3a 55%,#1e1e1e 100%);text-align:center;color:var(--white)}
.projects .lead{position:absolute;top:110px;width:100%;font-family:"Oswald",sans-serif;font-size:40px;font-weight:400}
.projects .claim{position:absolute;top:162px;width:100%;font-family:"Oswald",sans-serif;font-size:64px;font-weight:600;letter-spacing:1px}
.btn-estimate{position:absolute;top:270px;left:536px;width:128px;height:40px;background:var(--warm-grey);font-size:13px;line-height:40px}
.contact{position:absolute;top:1640px;left:80px;width:1040px}
.contact h3{font-size:22px;font-weight:400;color:#444;margin-top:22px}
.contact h3 b{font-weight:700;color:var(--charcoal)}
.contact .note{font-size:13px;color:#777;line-height:20px;width:640px;margin-top:12px}
.form{position:absolute;top:120px;left:0;width:660px}
.field{position:absolute;left:0;width:290px;height:36px;border:1px solid var(--line);font-size:12px;color:#aaa;padding:9px 12px}
.message{position:absolute;left:326px;top:0;width:306px;height:180px;border:1px solid var(--line);font-size:12px;color:#aaa;padding:9px 12px}
.btn-send{position:absolute;top:200px;left:0;width:78px;height:34px;background:var(--charcoal);color:var(--white);font-size:13px;font-weight:600;text-align:center;line-height:34px}
.details{position:absolute;top:0;left:752px;width:308px;height:268px;background:var(--warm-grey);color:var(--white);padding:22px 28px}
.details h4{font-size:22px;font-weight:400;border-bottom:1px solid #a89c8d;padding-bottom:12px;margin-bottom:16px}
.detail{display:flex;gap:12px;font-size:13px;line-height:18px;margin-bottom:12px;align-items:flex-start}
.detail svg{flex:none;margin-top:2px}
.site-footer{position:absolute;top:2020px;left:0;width:1200px;height:184px;background:var(--footer);color:#ddd;text-align:center}
.footer-nav{margin-top:42px;font-size:14px;display:flex;justify-content:center;gap:12px}
.footer-nav i{font-style:normal;color:#777}
.copyright{font-size:12px;color:#aaa;margin-top:10px}
.social{display:flex;justify-content:center;gap:10px;margin-top:30px}
.social span{width:28px;height:28px;border-radius:50%;background:#ddd}
</style>
</head>
<body>
<header class="site-header">
  <div class="brand"><span class="brand-mark"></span><span class="brand-name">Quil</span></div>
  <div class="top-bar">
    <span class="phone"><svg width="14" height="14" viewBox="0 0 24 24"><path fill="#877A69" d="M6.6 10.8a15 15 0 0 0 6.6 6.6l2.2-2.2a1 1 0 0 1 1-.25 11 11 0 0 0 3.6.6 1 1 0 0 1 1 1V20a1 1 0 0 1-1 1A17 17 0 0 1 3 4a1 1 0 0 1 1-1h3.5a1 1 0 0 1 1 1c0 1.25.2 2.45.57 3.57a1 1 0 0 1-.25 1z"/></svg>Call : 1300 555 014</span>
    <span class="login"><svg width="11" height="13" viewBox="0 0 11 13"><rect x="0" y="5.5" width="11" height="7.5" fill="#fff"/><path d="M2.5 5.5V3.5a3 3 0 0 1 6 0v2" stroke="#fff" stroke-width="1.5" fill="none"/></svg>Login</span>
  </div>
  <nav class="main-nav"><span>IT support</span><span>VoIP</span><span>Internet and Data</span><span>Cloud hosting</span><span>About</span><span>Contact</span></nav>
</header>

<div class="hero" role="img" aria-label="Business people in dark suits reviewing printed bar charts on a white meeting table with coffee cups"></div>

<section class="intro">
  <h1>IT outsourcing the way it should be</h1>
  <p>Not only does Quil have highly qualified people, with certifications from Corvane, Netrix, Halvern Telecom Registry amongst others, but importantly we can speak plain English and translate IT questions into a language you can understand and make decisions easier for you. We pride ourselves in our skill, integrity and ability to think and act in your best interests - that's what gets us customer referrals time after time.</p>
</section>

<section class="services">
  <article class="service">
    <div class="service-image" role="img" aria-label="Hand holding a tablet showing data charts"></div>
    <div class="service-body"><h2>DATA AND VOICE</h2><p>Quil provides a wide range of business data connections which are reliable, scalable, fast and represent excellent value for money. Choose from a wide range of fully managed options and plans.</p></div>
  </article>
  <article class="service">
    <div class="service-image" role="img" aria-label="Team working at computers in a modern office"></div>
    <div class="service-body"><h2>CLOUD SERVICES</h2><p>Quil provides a range of cloud services, including Software as a Service, Infrastructure as a Service and Platform as a Service.</p></div>
  </article>
  <article class="service">
    <div class="service-image" role="img" aria-label="Support staff gathered around a desk"></div>
    <div class="service-body"><h2>SUPPORT</h2><p>A wide range of skills and certifications with a good bedside manner. Service done on an on-call basis. Only pay for what you need, when you need it.</p></div>
  </article>
</section>

<section class="projects" role="img" aria-label="Silhouettes of a business team standing against a bright window">
  <div class="lead">Successfully Delivering Projects</div>
  <div class="claim">FOR NEW AND REPEAT CLIENTS</div>
  <div class="btn-estimate">Get Free Estimate!</div>
</section>

<section class="contact">
  <h3>You have questions? <b>AND NEED MORE HELP?</b></h3>
  <p class="note">No time to read all the information? That is quite normal. Continue focusing on your business and let us help you growing your services. Contact immediately one of our experienced advisers.</p>
  <div class="form">
    <div class="field" style="top:0">Your name</div>
    <div class="field" style="top:48px">Your email</div>
    <div class="field" style="top:96px">Your website</div>
    <div class="field" style="top:144px">Your subject</div>
    <div class="message">How can we help ?</div>
    <div class="btn-send">SEND</div>
  </div>
  <aside class="details">
    <h4>CONTACT DETAILS</h4>
    <div class="detail"><svg width="12" height="16" viewBox="0 0 12 16"><path fill="#fff" d="M6 0a6 6 0 0 0-6 6c0 4.5 6 10 6 10s6-5.5 6-10a6 6 0 0 0-6-6zm0 8.5A2.5 2.5 0 1 1 6 3.5a2.5 2.5 0 0 1 0 5z"/></svg><span>Street Address<br>Suite 6, 18-20 Harlow St<br>Kellham NSW 2761</span></div>
    <div class="detail"><svg width="14" height="14" viewBox="0 0 14 14"><circle cx="7" cy="7" r="6" fill="none" stroke="#fff" stroke-width="1.4"/><path d="M1 7h12M7 1c-3 3.5-3 8.5 0 12M7 1c3 3.5 3 8.5 0 12" stroke="#fff" fill="none"/></svg><span>http://www.quilmo.net</span></div>
    <div class="detail"><svg width="14" height="14" viewBox="0 0 24 24"><path fill="#fff" d="M6.6 10.8a15 15 0 0 0 6.6 6.6l2.2-2.2a1 1 0 0 1 1-.25 11 11 0 0 0 3.6.6 1 1 0 0 1 1 1V20a1 1 0 0 1-1 1A17 17 0 0 1 3 4a1 1 0 0 1 1-1h3.5a1 1 0 0 1 1 1c0 1.25.2 2.45.57 3.57a1 1 0 0 1-.25 1z"/></svg><span>T: +61 (2) 5550 1840</span></div>
    <div class="detail"><svg width="14" height="14" viewBox="0 0 24 24"><path fill="#fff" d="M6.6 10.8a15 15 0 0 0 6.6 6.6l2.2-2.2a1 1 0 0 1 1-.25 11 11 0 0 0 3.6.6 1 1 0 0 1 1 1V20a1 1 0 0 1-1 1A17 17 0 0 1 3 4a1 1 0 0 1 1-1h3.5a1 1 0 0 1 1 1c0 1.25.2 2.45.57 3.57a1 1 0 0 1-.25 1z"/></svg><span>F: +61 (2) 5550 1841</span></div>
    <div class="detail"><svg width="14" height="12" viewBox="0 0 14 12"><rect x="0.7" y="0.7" width="12.6" height="10.6" fill="none" stroke="#fff" stroke-width="1.4"/><path d="M1 1l6 5 6-5" stroke="#fff" stroke-width="1.4" fill="none"/></svg><span>Email: info@quilmo.net</span></div>
  </aside>
</section>

<footer class="site-footer">
  <nav class="footer-nav"><span>IT support</span><i>|</i><span>VoIP</span><i>|</i><span>Internet and Data</span><i>|</i><span>Cloud hosting</span><i>|</i><span>About</span><i>|</i><span>Contact</span></nav>
  <p class="copyright">Copyright 2017 © www.quilmo.net. All Rights Reserved</p>
  <div class="social"><span></span><span></span><span></span><span></span></div>
</footer>
</body>
</html>
```